New business card/stationary for a consulting company

I am looking for a clean and very professional looking business card for my consulting company as well as corresponding stationary. I am uploading our logo. I like simple and powerful for the feel. No graphics but I am open on everything else. Below is my contact information but would like the final to be in a version I can add my employees information into and print. Thank you.

Daniel Whitcombe
dan@fernlowadvisory.com
2837 North 9th Avenue, Summit Floor, Elm Ridge, Illinois 60483
www.fernlowadvisory.com

Industry/Entity Type

Consulting

Contact Information for Business Card

Daniel Whitcombe
dan@fernlowadvisory.com
www.fernlowadvisory.com

Font styles to use
Serif
Sans Serif

Requirements
Must have
• Our logo and the business card details.
Nice to have
• our website www.fernlowadvisory.com

```html
<!DOCTYPE html>
<html lang="en">
<head>
<meta charset="utf-8">
<title>Fernlow Advisory – Business Card</title>
<link rel="stylesheet" href="https://fonts.googleapis.com/css2?family=EB+Garamond:wght@400;700&family=Questrial&display=swap">
<style>
  :root {
    --navy: #0a0870;
    --navy-band: #1c1a66;
    --paper: #ffffff;
    --backdrop: #e6e9ea;
    --rule: #6b6b78;
    --ink: #1a1a2a;
  }
  * { box-sizing: border-box; margin: 0; padding: 0; }
  html, body { width: 1200px; height: 900px; overflow: hidden; }
  body {
    background: var(--backdrop);
    display: flex;
    flex-direction: column;
    align-items: center;
    justify-content: center;
    gap: 60px;
  }
  .card {
    width: 560px;
    height: 320px;
    position: relative;
    box-shadow: 0 6px 18px rgba(0,0,0,0.12);
  }

  /* Front */
  .card-front {
    background: var(--navy);
    display: flex;
    align-items: center;
    justify-content: center;
  }
  .brand {
    display: flex;
    align-items: center;
    gap: 16px;
    font-family: "Questrial", sans-serif;
    letter-spacing: 0.08em;
    text-transform: uppercase;
  }
  .brand-mark { display: block; }
  .card-front .brand { color: var(--paper); font-size: 30px; }
  .card-front .brand-mark { width: 30px; height: 30px; background: var(--paper); }

  /* Back */
  .card-back { background: var(--paper); }
  .band {
    position: absolute;
    left: 0;
    right: 0;
    height: 22px;
    background: var(--navy-band);
  }
  .band::after {
    content: "";
    position: absolute;
    left: 0;
    right: 0;
    height: 3px;
    background: var(--paper);
  }
  .band-top { top: 0; }
  .band-top::after { bottom: 5px; }
  .band-bottom { bottom: 0; }
  .band-bottom::after { top: 5px; }

  .back-layout {
    position: absolute;
    inset: 22px 0;
    display: flex;
    align-items: center;
  }
  .back-brand {
    flex: 0 0 285px;
    display: flex;
    justify-content: center;
  }
  .card-back .brand { color: var(--navy); font-size: 19px; gap: 10px; }
  .card-back .brand-mark { width: 19px; height: 19px; background: var(--navy); }

  .divider {
    width: 1px;
    height: 120px;
    background: var(--rule);
  }
  .contact {
    padding-left: 28px;
    font-family: "EB Garamond", serif;
    color: var(--ink);
    font-size: 13px;
    line-height: 1.3;
  }
  .contact-name {
    font-weight: 700;
    font-size: 18px;
    margin-bottom: 10px;
  }
  .contact-address { margin-bottom: 12px; }
  .contact-line {
    display: flex;
    align-items: center;
    gap: 6px;
  }
  .contact-line svg { width: 10px; height: 10px; flex: none; }
</style>
</head>
<body>

  <section class="card card-front">
    <div class="brand">
      <span class="brand-mark"></span>
      <span class="brand-name">Fernlow Advisory</span>
    </div>
  </section>

  <section class="card card-back">
    <div class="band band-top"></div>
    <div class="back-layout">
      <div class="back-brand">
        <div class="brand">
          <span class="brand-mark"></span>
          <span class="brand-name">Fernlow Advisory</span>
        </div>
      </div>
      <div class="divider"></div>
      <div class="contact">
        <p class="contact-name">Daniel Whitcombe</p>
        <p class="contact-address">2837 North 9th Avenue, Summit Floor<br>Elm Ridge, Illinois 60483</p>
        <p class="contact-line">
          <svg viewBox="0 0 10 10" aria-hidden="true"><rect x="0.5" y="2" width="9" height="6" fill="#1a1a2a"/><path d="M0.5 2 L5 5.5 L9.5 2" stroke="#fff" stroke-width="0.8" fill="none"/></svg>
          dan@fernlowadvisory.com
        </p>
        <p class="contact-line">
          <svg viewBox="0 0 10 10" aria-hidden="true"><circle cx="5" cy="5" r="4.3" fill="none" stroke="#1a1a2a" stroke-width="0.9"/><ellipse cx="5" cy="5" rx="1.8" ry="4.3" fill="none" stroke="#1a1a2a" stroke-width="0.7"/><path d="M0.7 5 H9.3" stroke="#1a1a2a" stroke-width="0.7"/></svg>
          www.fernlowadvisory.com
        </p>
      </div>
    </div>
    <div class="band band-bottom"></div>
  </section>

</body>
</html>
```